Upscale dog care facility need some marketing material

We offer a lot of services for dogs and their humans. We have a large indoor dog park, swimming pools, dog daycare and boarding, Pet CPR/First Aid classes and training. We love the trifold brochures where we can highlight all of our services (even a few pics of the facility) as well as give everyone information on our pricing and membership concepts. Will primarily be used for marketing to vets and local pet stores to help get the word out about our business.

```html
<!DOCTYPE html>
<html lang="en">
<head>
<meta charset="utf-8">
<title>Dog Daycare Trifold Brochure</title>
<link rel="stylesheet" href="https://fonts.googleapis.com/css2?family=Fredoka:wght@500;600;700&family=Montserrat:wght@300;400;500;600&display=swap">
<style>
  :root {
    --magenta: #c8177a;
    --orange: #f8ae3c;
    --orange-light: #fbc25e;
    --yellow: #f6eea4;
    --yellow-light: #fdf7b6;
    --teal: #2db89c;
    --teal-dark: #1f9a80;
    --white: #ffffff;
    --ink: #2a2a2a;
    --page: #6a6a6a;
    --display: "Fredoka", sans-serif;
    --body: "Montserrat", sans-serif;
  }
  * { box-sizing: border-box; margin: 0; padding: 0; }
  html, body { width: 797px; height: 1200px; overflow: hidden; }
  body { background: var(--page); font-family: var(--body); position: relative; }

  .brochure { position: absolute; left: 61px; width: 674px; height: 477px; overflow: hidden; }
  .brochure--outside { top: 80px; }
  .brochure--inside { top: 641px; }
  .brochure__art { position: absolute; inset: 0; }
  .block { position: absolute; }

  /* outside spread */
  .intro-title { left: 23px; top: 20px; width: 190px; font: 600 13px/1.12 var(--display); color: var(--white); }
  .feature-text { left: 121px; width: 92px; font: 500 6.3px/7.9px var(--body); color: var(--white); }
  .closing-title { left: 23px; top: 386px; width: 190px; font: 600 11px/1.15 var(--display); color: var(--white); }
  .closing-text { left: 23px; top: 424px; width: 182px; font: 500 6.1px/8px var(--body); color: var(--white); }

  .about-title { left: 224px; top: 176px; width: 225px; text-align: center; font: 600 20px/1 var(--display); color: var(--magenta); }
  .about-rule { left: 254px; top: 208px; width: 165px; height: 1px; background: var(--teal); }
  .about-text { left: 240px; top: 220px; width: 193px; text-align: center; font: 500 8px/9.8px var(--body); color: var(--ink); }
  .contact { left: 224px; top: 392px; width: 225px; text-align: center; font: 400 7px/1.2 var(--body); color: var(--white); }
  .contact__line { display: flex; align-items: center; justify-content: center; gap: 3px; margin-top: 4px; }
  .contact__line svg { width: 7px; height: 7px; }
  .contact__pin { width: 9px; height: 10px; display: block; margin: 0 auto 4px; }

  .cover-title { left: 449px; top: 24px; width: 225px; text-align: center; font: 700 46px/0.92 var(--display); color: var(--white); letter-spacing: -0.5px; }
  .cover-sub { left: 449px; top: 334px; width: 225px; text-align: center; font: 600 24px/1.08 var(--display); color: var(--magenta); }
  .cover-phone-rule { left: 486px; top: 404px; width: 151px; display: flex; align-items: center; gap: 8px; }
  .cover-phone-rule span { flex: 1; height: 1px; background: var(--white); }
  .cover-phone-rule svg { width: 12px; height: 12px; }
  .cover-phone { left: 449px; top: 416px; width: 225px; text-align: center; font: 600 24px/1 var(--display); color: var(--white); letter-spacing: 0.5px; }
  .cover-web { left: 449px; top: 446px; width: 225px; text-align: center; font: 600 10.5px/1 var(--body); color: var(--white); letter-spacing: 1.6px; }

  /* inside spread */
  .why-title { left: 30px; top: 219px; font: 600 22px/1 var(--display); color: var(--magenta); }
  .why-rule { left: 30px; top: 250px; width: 171px; height: 1px; background: var(--teal); }
  .why-text { left: 30px; top: 262px; width: 172px; font: 500 6.8px/8.9px var(--body); color: var(--ink); }

  .quote-mark { font: 700 40px/1 var(--display); color: var(--teal-dark); }
  .quote-open { top: 398px; }
  .quote-close { top: 438px; }
  .quote-text { top: 428px; width: 168px; font: 500 5.9px/7px var(--body); color: var(--white); }
  .quote-name { top: 453px; font: 500 6.3px/1 var(--body); color: var(--white); letter-spacing: 0.3px; }

  .section-title { font: 700 21px/1.05 var(--display); color: var(--white); letter-spacing: 0.3px; }
  .services-title { left: 248px; top: 17px; }
  .services-rule { left: 248px; top: 47px; width: 184px; height: 1px; background: var(--white); }
  .service { left: 311px; width: 125px; font: 300 14px/16.8px var(--body); color: var(--white); }
  .service-rule { left: 311px; width: 117px; height: 1px; background: var(--white); }
  .service-photo { position: absolute; width: 50px; height: 50px; border-radius: 50%; border: 1.5px solid var(--white); }

  .pricing-title { left: 471px; top: 17px; }
  .pricing-rule { left: 471px; top: 74px; width: 184px; height: 1px; background: var(--white); }
  .price-badge { left: 471px; width: 62px; height: 27px; border-radius: 2px; background: linear-gradient(100deg, var(--orange) 0%, var(--orange) 62%, var(--orange-light) 63%, var(--orange) 100%); font: 700 21px/27px var(--display); color: var(--white); text-align: center; }
  .price-name { left: 549px; font: 600 15px/27px var(--display); color: var(--white); }
  .price-text { left: 471px; width: 190px; font: 500 6.3px/7.8px var(--body); color: var(--white); }
</style>
</head>
<body>

<!-- Outside spread -->
<section class="brochure brochure--outside">
  <svg class="brochure__art" viewBox="0 0 674 477" width="674" height="477">
    <defs>
      <path id="arch" d="M0,0.78 C0,0.25 0.2,0 0.5,0 C0.8,0 1,0.25 1,0.78 C1,0.95 0.85,1 0.7,0.93 C0.55,0.86 0.45,0.86 0.3,0.93 C0.15,1 0,0.95 0,0.78 Z"/>
      <linearGradient id="yellowPanel" x1="0" y1="0" x2="1" y2="0">
        <stop offset="0" stop-color="#f3eb9f"/><stop offset="1" stop-color="#fdf7b0"/>
      </linearGradient>
    </defs>
    <rect width="674" height="477" fill="var(--orange)"/>
    <path d="M0,0 H224.5 V395 C150,395 60,330 0,273 Z" fill="var(--magenta)"/>
    <path d="M224.5,0 H449 V300 C380,345 300,395 224.5,395 Z" fill="url(#yellowPanel)"/>
    <path d="M449,0 H674 V314 C620,290 540,288 449,300 Z" fill="var(--teal)"/>
    <path d="M0,283 C60,345 150,407 224,407 C300,407 380,352 449,306 C540,276 620,292 674,316" fill="none" stroke="var(--magenta)" stroke-width="1.2" stroke-dasharray="3 2"/>
    <line x1="224.5" y1="0" x2="224.5" y2="477" stroke="#000" stroke-opacity="0.05"/>
    <line x1="449" y1="0" x2="449" y2="477" stroke="#000" stroke-opacity="0.05"/>

    <!-- feature circles -->
    <g fill="none" stroke="var(--white)" stroke-width="1" stroke-dasharray="2 2">
      <circle cx="64" cy="107" r="45"/><circle cx="64" cy="217" r="45"/><circle cx="64" cy="327" r="45"/>
    </g>
    <circle role="img" aria-label="Photo: vet examining a dog" cx="64" cy="107" r="38" fill="#dfe6ee" stroke="var(--white)" stroke-width="3"/>
    <circle role="img" aria-label="Photo: vet treating a small dog" cx="64" cy="217" r="38" fill="#cfdde9" stroke="var(--white)" stroke-width="3"/>
    <circle role="img" aria-label="Photo: vets with a shepherd dog" cx="64" cy="327" r="38" fill="#c9b7a4" stroke="var(--white)" stroke-width="3"/>
    <g>
      <circle cx="33" cy="81" r="10" fill="var(--teal)"/><path d="M28,81 l3.5,3.5 l6.5,-7" fill="none" stroke="#fff" stroke-width="2" stroke-linecap="round" stroke-linejoin="round"/>
      <circle cx="33" cy="191" r="10" fill="var(--teal)"/><path d="M28,191 l3.5,3.5 l6.5,-7" fill="none" stroke="#fff" stroke-width="2" stroke-linecap="round" stroke-linejoin="round"/>
      <circle cx="33" cy="301" r="10" fill="var(--teal)"/><path d="M28,301 l3.5,3.5 l6.5,-7" fill="none" stroke="#fff" stroke-width="2" stroke-linecap="round" stroke-linejoin="round"/>
    </g>

    <!-- about arch -->
    <use href="#arch" transform="translate(240,19) scale(197,158)" fill="none" stroke="var(--teal)" stroke-width="0.006" stroke-dasharray="0.012 0.008"/>
    <use href="#arch" role="img" aria-label="Photo: puppy and kitten cuddling" transform="translate(248,26) scale(181,143)" fill="#f1f1f1" stroke="var(--orange)" stroke-width="0.025"/>
    <ellipse role="img" aria-label="Photo: white labrador puppy lying down" cx="322" cy="340" rx="76" ry="44" fill="#f2ece0"/>

    <!-- cover arch -->
    <use href="#arch" transform="translate(452,137) scale(224,183)" fill="none" stroke="var(--white)" stroke-width="0.006" stroke-dasharray="0.012 0.008"/>
    <use href="#arch" role="img" aria-label="Photo: woman hugging a white puppy" transform="translate(462,146) scale(203,162)" fill="#d7d0c6" stroke="var(--magenta)" stroke-width="0.028"/>
  </svg>

  <h2 class="block intro-title">Lorem ipsum dolor sit amet, consectetur adipiscing elit</h2>
  <p class="block feature-text" style="top:76px">sed do eiusmod tempor incididunt ut labore et dolore magna aliqua. Ut enim ad minim veniam, quis nostrud exercitation ullamco laboris nisi ut aliquip ex ea commodo consequat.</p>
  <p class="block feature-text" style="top:186px">sed do eiusmod tempor incididunt ut labore et dolore magna aliqua. Ut enim ad minim veniam, quis nostrud exercitation ullamco laboris nisi ut aliquip ex ea commodo consequat.</p>
  <p class="block feature-text" style="top:296px">sed do eiusmod tempor incididunt ut labore et dolore magna aliqua. Ut enim ad minim veniam, quis nostrud exercitation ullamco laboris nisi ut aliquip ex ea commodo consequat.</p>
  <h3 class="block closing-title">Lorem ipsum dolor<br>sit amet, consectetur adipiscing</h3>
  <p class="block closing-text">sed do eiusmod tempor incididunt ut labore et dolore magna aliqua. Ut enim ad minim veniam, quis nostrud exercitation ullamco laboris nisi ut aliquip ex ea commodo consequat.</p>

  <h2 class="block about-title">About Us</h2>
  <div class="block about-rule"></div>
  <p class="block about-text">Lorem ipsum dolor sit amet, consectetur adipiscing elit, sed do eiusmod tempor incididunt ut labore et dolore magna aliqua. Ut enim ad minim veniam, quis nostrud exercitation ullamco laboris nisi ut aliquip ex ea commodo consequat.</p>

  <address class="block contact" style="font-style:normal">
    <svg class="contact__pin" viewBox="0 0 10 12"><path d="M5,1 a3,3 0 1 1 0,6 a3,3 0 1 1 0,-6 M5,7 V11 M2,11 H8" fill="none" stroke="var(--magenta)" stroke-width="1.3"/></svg>
    <div>address line 1, address line 1, address line 1,<br>address line 2.</div>
    <div class="contact__line"><svg viewBox="0 0 8 8"><rect x="0.5" y="1.5" width="7" height="5" fill="none" stroke="var(--magenta)" stroke-width="0.8"/><path d="M0.5,1.5 L4,4.5 L7.5,1.5" fill="none" stroke="var(--magenta)" stroke-width="0.8"/></svg>hello@pawhavenclub.com</div>
    <div class="contact__line"><svg viewBox="0 0 8 8"><circle cx="4" cy="4" r="3.5" fill="none" stroke="var(--magenta)" stroke-width="0.8"/><path d="M2.6,2.4 q0,3 3,3.2 l0.4,-0.8 l-1,-0.5 l-0.4,0.4 q-1,-0.4 -1.2,-1.3 l0.4,-0.4 l-0.5,-1 z" fill="var(--magenta)"/></svg>0198 765 432</div>
    <div class="contact__line"><svg viewBox="0 0 8 8"><circle cx="4" cy="4" r="3.5" fill="none" stroke="var(--magenta)" stroke-width="0.8"/><ellipse cx="4" cy="4" rx="1.5" ry="3.5" fill="none" stroke="var(--magenta)" stroke-width="0.6"/><line x1="0.5" y1="4" x2="7.5" y2="4" stroke="var(--magenta)" stroke-width="0.6"/></svg>www.pawhavenclub.com</div>
  </address>

  <h1 class="block cover-title">dog<br>daycare</h1>
  <h2 class="block cover-sub">dog daycare<br>and boarding</h2>
  <div class="block cover-phone-rule"><span></span><svg viewBox="0 0 12 12"><circle cx="6" cy="6" r="5.3" fill="none" stroke="#fff" stroke-width="0.9"/><path d="M4,3.5 q0,4.5 4.5,4.8 l0.5,-1.1 l-1.4,-0.7 l-0.6,0.6 q-1.5,-0.6 -1.8,-1.9 l0.6,-0.6 l-0.7,-1.4 z" fill="#fff"/></svg><span></span></div>
  <p class="block cover-phone">0198 765 432</p>
  <p class="block cover-web">www.pawhavenclub.com</p>
</section>

<!-- Inside spread -->
<section class="brochure brochure--inside">
  <svg class="brochure__art" viewBox="0 0 674 477" width="674" height="477">
    <defs>
      <path id="archIn" d="M0,0.78 C0,0.25 0.2,0 0.5,0 C0.8,0 1,0.25 1,0.78 C1,0.95 0.85,1 0.7,0.93 C0.55,0.86 0.45,0.86 0.3,0.93 C0.15,1 0,0.95 0,0.78 Z"/>
    </defs>
    <rect x="0" width="225" height="477" fill="var(--yellow)"/>
    <rect x="224.5" width="225" height="477" fill="var(--orange)"/>
    <rect x="449" width="225" height="477" fill="var(--magenta)"/>
    <path d="M0,309 C60,360 150,400 224,400 C300,400 380,320 449,278 C520,242 600,250 674,262 V477 H0 Z" fill="var(--teal)"/>
    <path d="M0,321 C60,372 150,412 224,412 C300,412 380,333 449,291 C520,256 600,264 674,274" fill="none" stroke="var(--white)" stroke-width="1.1" stroke-dasharray="3 2"/>

    <use href="#archIn" transform="translate(10,14) scale(240,196)" fill="none" stroke="var(--teal)" stroke-width="0.006" stroke-dasharray="0.012 0.008"/>
    <use href="#archIn" role="img" aria-label="Photo: puppy lying on green grass" transform="translate(17,22) scale(226,180)" fill="#7fa834" stroke="var(--magenta)" stroke-width="0.028"/>

    <circle role="img" aria-label="Photo: woman with a white dog" cx="72" cy="366" r="36" fill="#e9ddd2" stroke="var(--magenta)" stroke-width="3"/>
    <circle role="img" aria-label="Photo: woman with a small dog among flowers" cx="326" cy="372" r="36" fill="#8aa14e" stroke="var(--magenta)" stroke-width="3"/>

    <use href="#archIn" transform="translate(440,268) scale(258,214)" fill="none" stroke="var(--white)" stroke-width="0.006" stroke-dasharray="0.012 0.008"/>
    <use href="#archIn" role="img" aria-label="Photo: woman giving a high five to a golden retriever" transform="translate(449,276) scale(238,196)" fill="#c9a27c" stroke="var(--orange)" stroke-width="0.024"/>
  </svg>

  <h2 class="block why-title">Why Us</h2>
  <div class="block why-rule"></div>
  <p class="block why-text">Lorem ipsum dolor sit amet, consectetur adipiscing elit, sed do eiusmod tempor incididunt ut labore et dolore magna aliqua. Ut enim ad minim veniam, quis nostrud exercitation ullamco laboris nisi ut aliquip ex ea commodo consequat. Duis aute irure dolor in reprehenderit in voluptate velit esse cillum dolore eu fugiat nulla pariatur.</p>

  <span class="block quote-mark quote-open" style="left:28px">“</span>
  <p class="block quote-text" style="left:30px">sed do eiusmod tempor incididunt ut labore et dolore magna aliqua. Ut enim ad minim veniam, quis nostrud exercitation ullamco laboris nisi ut aliquip ex ea commodo consequat.</p>
  <p class="block quote-name" style="left:132px">MARA LIND</p>
  <span class="block quote-mark quote-close" style="left:173px">”</span>

  <span class="block quote-mark quote-open" style="left:252px">“</span>
  <p class="block quote-text" style="left:254px">sed do eiusmod tempor incididunt ut labore et dolore magna aliqua. Ut enim ad minim veniam, quis nostrud exercitation ullamco laboris nisi ut aliquip ex ea commodo consequat.</p>
  <p class="block quote-name" style="left:356px">MARA LIND</p>
  <span class="block quote-mark quote-close" style="left:397px">”</span>

  <h2 class="block section-title services-title">OUR SERVICES</h2>
  <div class="block services-rule"></div>
  <div class="service-photo" role="img" aria-label="Photo: dogs playing in the indoor park" style="left:249px;top:61px;background:#3f6b4a"></div>
  <div class="service-photo" role="img" aria-label="Photo: dog swimming in a pool" style="left:249px;top:120px;background:#2c6fb5"></div>
  <div class="service-photo" role="img" aria-label="Photo: dogs in the daycare room" style="left:249px;top:180px;background:#bdb6ae"></div>
  <div class="service-photo" role="img" aria-label="Photo: dog training class outdoors" style="left:249px;top:248px;background:#9bb07a"></div>
  <p class="block service" style="top:77px">Large Indoor<br>Dog Park</p>
  <div class="block service-rule" style="top:117px"></div>
  <p class="block service" style="top:137px">Swimming<br>Pools</p>
  <div class="block service-rule" style="top:175px"></div>
  <p class="block service" style="top:195px">Dog Daycare<br>and Boarding</p>
  <div class="block service-rule" style="top:235px"></div>
  <p class="block service" style="top:256px">Pet Cpr/First Aid<br>Classes<br>And Training</p>

  <h2 class="block section-title pricing-title">PRICING &amp;<br>MEMBERSHIP</h2>
  <div class="block pricing-rule"></div>

  <p class="block price-badge" style="top:83px">$199</p>
  <p class="block price-name" style="top:83px">Lorem ipsum</p>
  <p class="block price-text" style="top:116px">sed do eiusmod tempor incididunt ut labore et dolore magna aliqua. Ut enim ad minim veniam,</p>

  <p class="block price-badge" style="top:138px">$199</p>
  <p class="block price-name" style="top:138px">Lorem ipsum</p>
  <p class="block price-text" style="top:171px">sed do eiusmod tempor incididunt ut labore et dolore magna aliqua. Ut enim ad minim veniam,</p>

  <p class="block price-badge" style="top:194px">$199</p>
  <p class="block price-name" style="top:194px">Lorem ipsum</p>
  <p class="block price-text" style="top:227px">sed do eiusmod tempor incididunt ut labore et dolore magna aliqua. Ut enim ad minim veniam,</p>
</section>

</body>
</html>
```